TRV Business Card

Business card design for a handyman company. Want to portray a professional image and stay away from the "Mom & Pops" image that is normally associated with handyman companies.

Business

```html
<!DOCTYPE html>
<html lang="en">
<head>
<meta charset="utf-8">
<title>TRV Business Card</title>
<link href="https://fonts.googleapis.com/css2?family=Philosopher:ital,wght@0,700;1,700&family=Questrial&display=swap" rel="stylesheet">
<style>
  :root {
    --page: #ffffff;
    --card: #c6e2ef;
    --tools: #7fa6c6;
    --navy: #13253d;
    --teal: #1b3a3c;
    --ink: #2f3a40;
  }
  html, body {
    margin: 0;
    padding: 0;
    width: 1200px;
    height: 1200px;
    overflow: hidden;
    background: var(--page);
  }
  .card {
    position: absolute;
    left: 68px;
    top: 275px;
    width: 1068px;
    height: 607px;
    background: var(--card);
    overflow: hidden;
  }
  .tools-art {
    position: absolute;
    left: 37px;
    top: 108px;
    width: 450px;
    height: 499px;
    background: linear-gradient(180deg, rgba(127,166,198,0.55), rgba(127,166,198,0.35));
  }
  .brand-name {
    position: absolute;
    right: 40px;
    top: 18px;
    margin: 0;
    font-family: "Questrial", sans-serif;
    font-size: 150px;
    line-height: 1;
    letter-spacing: 14px;
    color: var(--navy);
  }
  .sector {
    position: absolute;
    left: 182px;
    top: 238px;
    margin: 0;
    font-family: "Philosopher", sans-serif;
    font-style: italic;
    font-weight: 700;
    font-size: 36px;
    color: var(--teal);
    text-decoration: underline;
    text-decoration-thickness: 2px;
    text-underline-offset: 5px;
  }
  .services {
    position: absolute;
    left: 26px;
    top: 320px;
    margin: 0;
    padding: 0;
    list-style: none;
    font-family: "Philosopher", sans-serif;
    font-weight: 700;
    font-size: 39px;
    line-height: 51px;
    color: var(--teal);
  }
  .services li::before {
    content: "";
    display: inline-block;
    width: 16px;
    height: 16px;
    margin-right: 8px;
    background: var(--teal);
    vertical-align: 4px;
  }
  .contact {
    position: absolute;
    right: 29px;
    top: 333px;
    margin: 0;
    font-style: normal;
    text-align: right;
    font-family: "Questrial", sans-serif;
    font-size: 37px;
    line-height: 51px;
    color: var(--ink);
  }
  .contact span { display: block; }
</style>
</head>
<body>
  <section class="card">
    <div class="tools-art" role="img" aria-label="Large outline illustration of a wrench and a hammer"></div>
    <h1 class="brand-name">TRV</h1>
    <p class="sector">Residential &amp; Commercial Services</p>
    <ul class="services">
      <li>Home Repairs</li>
      <li>Handyman Services</li>
      <li>Drain Cleaning</li>
      <li>Carpet Cleaning</li>
    </ul>
    <address class="contact">
      <span>4710 W Meadow Ln</span>
      <span>Hollis, Ks 66900</span>
      <span>(555) 318-4407 p</span>
      <span>(555) 318-4409 f</span>
      <span>info@TrvHomeCare.com</span>
    </address>
  </section>
</body>
</html>
```